Beautiful & Elegant Digital Brochure Needed For Luxury Real Estate Development

Hello,

Our company is seeking a beautiful design for our real estate development that is currently being launched.

About The Project:
Development Name - Willow Crest Estate
Location - Charleston, S.C.
Low-Country Southern Style Architecture
Google "low-country" Charleston, SC to get an idea of the unique culture of the city
Google "willow crest tree" Charleston, SC to understand the branding

Other Digital Brochures that we love

http://www.fernvalehotels.example/cedarhollow/wp-content/uploads/sites/6/2014/08/adventures-brochure.pdf

Why we like it... We love the classy feeling the brochure portrays by using unique fonts and backgrounds (burlap textures). We also love the images that represent a "low-country" vibe.

Requirements:
1. We will be providing all of the content (attached)

2. Please use plenty of southern low-country stock images from PixelVaultStock (we have a subscription so just use the watermarked images unless you have full permissions)

3. Do not copy the Cedar Hollow brochure - create a unique vision that fits in to the low-country and southern vibe

4. Attached is our logos

The font we like to use is - Caslon Antique / italic
Thank you!

Project Deadline Extended Reason: We've added more design information and we need to get more designers to participate. Added Monday, May 30, 2016

Target Market(s)

High net worth individuals - each homesite will be over 6 million dollars USD

Industry/Entity Type

Real Estate Development

Font styles to use
Script
Other font styles liked:
• Caslon Antique & Italic

Colors
abd036
00a990
acd036
9bcb3c
33b8a4
86cfc6
cfeae6

Requirements
Must have
• low country feeling
Nice to have
• burlap, wood backgrounds
Should not have
• Should NOT be corporate. This brochure is for multi-millionaire home buyers and investors. They are seeking simple, beautiful, quiet, serene, and southern lifestyles on the Intracoastal waterway on Marley Isle, Charleston, South Carolina.

```html
<!DOCTYPE html>
<html lang="en">
<head>
<meta charset="utf-8">
<title>Willow Crest Estate — Lowcountry Brochure</title>
<link href="https://fonts.googleapis.com/css2?family=IM+Fell+English:ital@0;1&family=Pinyon+Script&display=swap" rel="stylesheet">
<style>
:root{
  --stage:#d9d9d9;
  --paper:#ffffff;
  --ink:#1e1a16;
  --gold:#a9782f;
  --tan:#b39a73;
  --tan-deep:#a88d66;
  --bark:#5b3f25;
  --cream:#f6efe2;
}
*{margin:0;padding:0;box-sizing:border-box}
html,body{width:856px;height:1200px;overflow:hidden;background:var(--stage)}
body{position:relative;font-family:"IM Fell English",Georgia,serif;color:var(--ink)}
.spread{position:absolute;left:48px;width:760px;height:520px;background:var(--paper);box-shadow:0 4px 14px rgba(0,0,0,.18)}
.spread--welcome{top:30px}
.spread--attractions{top:642px}
.fold{position:absolute;left:379px;top:0;width:2px;height:100%;background:rgba(0,0,0,.06)}
.photo{position:absolute}
.page-bar{position:absolute;left:0;bottom:0;width:110px;height:14px;background:var(--bark)}
.heading{font-family:"IM Fell English",Georgia,serif;color:var(--gold);font-weight:400;line-height:1.35}
.heading .initial{font-family:"Pinyon Script",cursive;font-size:1.7em;line-height:0;margin-right:1px}
.body{font-size:6.4px;line-height:1.42;text-align:justify}
.body p+p{margin-top:9px}

/* spread 1 */
.welcome-title{position:absolute;left:30px;top:32px;width:200px;font-size:12px;text-align:center}
.welcome-copy{position:absolute;left:28px;top:92px;width:190px}
.photo--waterfront{left:226px;top:18px;width:516px;height:284px;background:linear-gradient(180deg,#4f8fc7 0%,#9ac4dc 28%,#e8c07c 46%,#c98d52 58%,#6bb3ad 70%,#e9cfb4 88%,#f2e3d2 100%)}
.photo--driftwood{left:226px;top:312px;width:142px;height:172px;background:linear-gradient(180deg,#6d7fa6 0%,#c89aa1 35%,#e9a86a 55%,#7d8aa4 75%,#3d4a63 100%)}
.panel--new-old{position:absolute;left:380px;top:310px;width:380px;height:210px;background:linear-gradient(180deg,var(--tan) 0%,var(--tan-deep) 100%);color:var(--cream)}
.panel--new-old .heading{position:absolute;left:14px;top:12px;font-size:11px;color:#7a5a2e}
.panel--new-old .col{position:absolute;top:42px;width:165px}
.panel--new-old .col--a{left:14px;color:#efe3cc}
.panel--new-old .col--b{left:200px;top:38px;color:#fff}

/* spread 2 */
.photo--oak{left:0;top:0;width:380px;height:250px;background:linear-gradient(135deg,#6b4a1e 0%,#a97a2e 30%,#e8c36a 55%,#f2dca0 70%,#8e6a2a 100%)}
.weather-title{position:absolute;left:40px;top:296px;font-size:11px}
.weather-copy{position:absolute;left:40px;top:328px;width:305px}
.strip--wood{position:absolute;left:422px;top:0;width:300px;height:22px;background:linear-gradient(90deg,#4a2e1a,#6e4a2e 40%,#553622 70%,#3e2616)}
.attractions-title{position:absolute;left:380px;top:52px;width:380px;text-align:center;font-size:13px}
.attractions-quote{position:absolute;left:410px;top:88px;width:320px;font-style:italic;font-size:7px;line-height:1.6;text-align:center}
.attractions-quote .mark{font-weight:bold;font-style:normal;font-size:9px}
.feature-title{position:absolute;font-size:9px}
.feature-copy{position:absolute}
.photo--brush{left:524px;top:155px;width:110px;height:122px;background:linear-gradient(135deg,#cfd8e2 0%,#6d9ac4 45%,#b08a5c 70%,#e5dccd 100%)}
.photo--pier{left:398px;top:370px;width:102px;height:66px;background:linear-gradient(180deg,#2e4d7d 0%,#7aa1c9 45%,#3b5f8e 70%,#1e3458 100%)}
.photo--street{left:646px;top:350px;width:104px;height:64px;background:linear-gradient(180deg,#7fb0dc 0%,#cfe2ee 35%,#d7b98c 60%,#8a8f6a 80%,#777 100%)}
.photo--marsh{left:380px;top:452px;width:380px;height:68px;background:linear-gradient(180deg,#c99c4e 0%,#e2c27f 40%,#a57a3a 100%)}
</style>
</head>
<body>

<section class="spread spread--welcome">
  <div class="fold"></div>
  <h1 class="heading welcome-title"><span class="initial">W</span>elcome to The Lowcountry, Where Tradition and Elegance Meet</h1>
  <div class="body welcome-copy">
    <p>Charleston has always embodied the geniality of the aristocratic South and has been a conspicuous epicenter for some of the country's finest art, architecture, and cultural resources. This is flawlessly illustrated by the concentration of exquisite historic structures located throughout the city and the surrounding countryside. The city's architectural heritage has been nurtured by many groups including Charleston's active and influential Heritage Keepers Society. The group, founded in 1920, is the oldest of its kind anywhere in the country. Owing to their ongoing efforts, the city's National Historic Landmark District has seen multiple expansions as restoration projects have materialized throughout the area. The group is committed to promoting the city's historical legacy through restorative projects, preservation initiatives, and education about the city's rich heritage.</p>
    <p>With new additions to the Historic Registry as recently as the 1980s, the city's ever-growing designated "Old and Historic District" has now expanded to cover 138 acres. Within these borders, nearly 5000 exquisitely preserved historic buildings stand as testament to the city's dedication to maintaining the beautiful architecture in and around the heart of the city. Picturesque examples from an array of architectural periods line city streets, beckoning tourists and inspiring awe in passers-by. Georgian, Regency, and Federal, as well as Classical, Greek, and Gothic Revivals are some of the more popular and most prominently featured styles but the city is host to many homes, shops, and civic buildings whose designs were inspired by other periods of architectural influence.</p>
    <p>While many buildings are being rehabilitated throughout the city, conservation efforts are also dedicated to preventing the further decline of surviving historic sites. Efforts to preserve original structures and their components have been hugely successful. Throughout the city, stunning historical features in pristine condition stand as a testament to dedicated conservators' efforts. Perhaps the most notable example is that some area homes still proudly feature their original crown glass windows, remarkably intact after hundreds of years. The antique glass was traditionally hand-blown by highly skilled artisans aided by experienced assistants. Due to the irregularities in thickness and density, the method resulted in a distinct, wavy optical quality that can be easily identified by the discerning eye.</p>
  </div>
  <div class="photo photo--waterfront" role="img" aria-label="Historic pastel mansions and palm trees along a harbour seawall at sunset, reflected in calm water"></div>
  <div class="photo photo--driftwood" role="img" aria-label="Bare driftwood tree standing in shallow water at sunrise"></div>
  <div class="panel--new-old">
    <h2 class="heading"><span class="initial">N</span>ew Meets Old</h2>
    <div class="body col col--a">
      <p>The Lowcountry boasts a proud tradition of refined Southern grace and charming appeal. Few cities have been able to blend this heirloom charm with modernity quite like Charleston, which has become a premium destination for those seeking to abandon the drab, predictable regularity that characterizes modern existence. For decades, the city has continually expanded, acquiring nearby land and enticing new residents seeking a diversion from the ordinary. While encouraging this growth, the city, local government, and residents remain steadfastly dedicated to maintaining the time-honored elegance of historic Charleston.</p>
    </div>
    <div class="body col col--b">
      <p>The city's continued commitment to historic accuracy is widely apparent. From the period-inspired colors of the hundreds of restored homes to the careful selection of traditional materials used for renovations, no detail has been spared to maintain the area's classic beauty. By incorporating authentic, period-era building materials such as tabby, brick, and locally-sourced hardwood, as well as staying true to certain architectural traditions, the city has been able to fuse modern luxury with the charming elegance of the quintessential South. Visitors will find that even the newest homes feature large, inviting porches, intricate trim and molding, and an attention to architectural detail that is often overlooked in modern construction.</p>
    </div>
  </div>
  <div class="page-bar"></div>
</section>

<section class="spread spread--attractions">
  <div class="fold"></div>
  <div class="photo photo--oak" role="img" aria-label="Sprawling live oak with golden light filtering across a sandy path"></div>
  <h2 class="heading weather-title"><span class="initial">L</span>et the Weather Draw You Out</h2>
  <div class="body weather-copy">
    <p>Thanks to the beautiful vistas and exceptionally good weather, the Lowcountry is a mecca for outdoor living. Because of Charleston's temperate climate, outdoor attractions are available year-round. The area boasts short, mild winters and long, hot summers. Measurable snowfall is rare, and the temperature rarely drops below freezing. Spring and fall are marked by comfortable, consistent temperatures that will coax you out of doors. Rich, well-draining soil and a consistent, temperate climate afford gardeners the luxury of a year round growing season and open the door to a wide array of landscaping options not readily enjoyed in many areas.</p>
    <p>For centuries, natives of the Lowcountry have designed their residences to take advantage of the region's enviable weather conditions and wind patterns. Large porches, sizable verandas and generous roof overhangs are conventional residential features allowing not only cover from the midday sun but also providing an ideal location to sip cocktails and entertain guests. Charlestonians relish the area's prevailing winds and their strong, cool breezes. These draft inland, sweeping through open air porches and wafting through open windows.</p>
  </div>
  <div class="page-bar"></div>

  <div class="strip--wood" role="img" aria-label="Weathered wood plank"></div>
  <h2 class="heading attractions-title"><span class="initial">C</span>harleston's Attractions</h2>
  <p class="attractions-quote"><span class="mark">“</span> Whatever your interests, the Lowcountry paradise has something for everyone. Charleston offers a multitude of unique attractions that simply must be seen. <span class="mark">”</span></p>

  <h3 class="heading feature-title" style="left:398px;top:150px"><span class="initial">L</span>earn About Marine Life</h3>
  <div class="body feature-copy" style="left:398px;top:172px;width:118px">
    <p>The city's expansive aquarium offers visitors a chance to enjoy the beauty of marine life first-hand. Featuring more than 5000 indigenous and exotic species of fish, reptile, and amphibians, the aquarium invites the curious and adventurous alike. Interactive exhibits encourage visitors to get up close and personal with wildlife that is rarely seen and often misunderstood. Bonnethead and cownose sharks, southern stingrays, starfish, hermit crabs, and sea urchins reside in large tanks with shallow pools designed to allow visitors to reach out and touch the animals. Enthusiastic volunteers are always nearby to guarantee safety and provide insight. The facility opens onto the adjoining harbor where bottlenose dolphins and sea turtles can be observed.</p>
  </div>
  <div class="photo photo--pier" role="img" aria-label="Long fishing pier stretching over the ocean at dusk"></div>

  <div class="photo photo--brush" role="img" aria-label="Paintbrush with blue paint on a textured palette"></div>
  <h3 class="heading feature-title" style="left:524px;top:290px"><span class="initial">A</span>rt in the City</h3>
  <div class="body feature-copy" style="left:524px;top:312px;width:112px">
    <p>In recent decades, a powerful cultural initiative has taken root in the city. Folk art and artisan crafts remain integral elements of the Charleston art scene. Arts festivals and events occur year-round and the multitude of galleries featuring original works from local and world-renowned artists is ever-expanding. Fine art galleries as well as those housing contemporary or modern works are scattered throughout the city. Open air exhibits and outdoor statue gardens provide an alternative way to experience the local culture while keeping the arts accessible to the public.</p>
  </div>

  <h3 class="heading feature-title" style="left:646px;top:150px"><span class="initial">T</span>he Sound of the City</h3>
  <div class="body feature-copy" style="left:646px;top:172px;width:106px">
    <p>Charleston's music scene is as diverse as every other aspect of the city and the venues are nearly as important as the music itself. Visit the historic Harborview Chapel for performances inspired by the Charleston's musical heritage. The group's weekly set includes gospel, jazz, slave songs, and Civil War era battle hymns. Visit a venue or, allow the music to come to you. Lowtide Chamber Ensemble is comprised of Lowcountry musicians with a passion for classical music. The group performs in homes, businesses, and concert halls. The Tidewater Symphony Orchestra performs September thru May.</p>
  </div>
  <div class="photo photo--street" role="img" aria-label="Pastel storefronts and a white church steeple on a historic street"></div>

  <div class="photo photo--marsh" role="img" aria-label="Close-up of golden dried marsh grass"></div>
</section>

</body>
</html>
```